Stationery using new logo for pharmacy and gift shop

We need a letterhead, business card, gift voucher and possibly compliments slip design for our pharmacy and gift shop using our new logo.
The letterhead would need to be produced in both colour (purple and green) and grayscale and the business card would preferably be one-sided, but can be two-sided if this works better with the information it needs to have on it.

We would like a simple and elegant design, but not so simple that it looks like we've done it ourselves on Word. Use of our colours would be great but the letterhead would need to look good if printed on our black and white laser printer. If this is not possible then an additional version for grayscale would be needed.

We would need to receive high quality files that we can work with easily, such as pdf's for the letterhead that we can print instantly or order online as it appears on screen and business cards in jpeg and pdf so we can upload to printing sites.
We would like the vouchers in denominations of £5 and £10 in A5 size in a printable format such as PDF so that we don't have to resize.

Letterhead is for use in correspondence and invoicing to patients, surgeries, traders, customers etc.

Our preferred font is Orkney

Letterhead Info
Address
47 Fenwick Rd.
Cockermouth
Cumbria
CA17 4TW

Tel: (01900) 357148
Fax: (01900) 364057
Website: www.brackenfieldpharmacy.com
Email: patientcare@brackenfieldpharmacy.com

Business Card Info.
As above but email address is: rtkdenholm@postbox-mail.co.uk

Voucher Info.
Small print to state that any change will be paid as a credit note.
Space for a staff member to sign, date and stamp voucher

I have quite a few logo files so please ask if you need more uploaded. Or if you need more information to improve the design then please contact me.

Target Market(s)

Both retail customers and professional colleagues

Industry/Entity Type

Pharmacy

Font styles to use
Other font styles liked:
• orkney

Colors
ffffff
9bcb3c
6b449b

Requirements
Must have
• Must be clear and legible with a professional feel. Must use the logo well and all aspects of the designs should work well together.
• Final files MUST be easy to use for non-computer specialists. I need staff to be able to pull up a letterhead template easily if they are writing a letter or raising an invoice. The business card must be in a format ready to be sent to print.
Nice to have
• Letterhead available in a word processor program like word so that letters can be sent by email as well as print or print and scan.

```html
<!DOCTYPE html>
<html lang="en">
<head>
<meta charset="utf-8">
<title>Brackenfield Chemist – Credit Note</title>
<link rel="stylesheet" href="https://fonts.googleapis.com/css2?family=Jost:wght@400;500;600&display=swap">
<style>
  :root {
    --purple: #6b449b;
    --green: #9bcb3c;
    --white: #ffffff;
    --backdrop: #ecebef;
    --rule-grey: #6b449b;
  }
  * { margin: 0; padding: 0; box-sizing: border-box; }
  html, body {
    width: 1200px;
    height: 960px;
    overflow: hidden;
    background: var(--backdrop);
    font-family: "Jost", "Century Gothic", sans-serif;
  }
  .credit-note {
    position: absolute;
    left: 263px;
    top: 243px;
    width: 674px;
    height: 474px;
    background: var(--white);
    box-shadow: 0 2px 10px rgba(40, 20, 70, 0.12);
    transform: scale(1.48);
    transform-origin: 50% 50%;
    color: var(--purple);
  }
  .brand {
    position: absolute;
    top: 40px;
    left: 0;
    width: 100%;
    text-align: center;
  }
  .brand-square {
    display: block;
    width: 46px;
    height: 46px;
    margin: 0 auto 36px;
    background: var(--purple);
  }
  .brand-name {
    font-size: 29px;
    font-weight: 400;
    letter-spacing: 0.2px;
    line-height: 1;
    color: var(--purple);
  }
  .title {
    position: absolute;
    top: 214px;
    left: 0;
    width: 100%;
    text-align: center;
    font-size: 94px;
    font-weight: 600;
    line-height: 1;
    letter-spacing: -0.5px;
    color: var(--purple);
  }
  .amount-rule {
    position: absolute;
    left: 85px;
    top: 354px;
    width: 505px;
    height: 2px;
    background: var(--green);
  }
  .sign-off {
    position: absolute;
    left: 86px;
    top: 416px;
    width: 505px;
    display: flex;
    align-items: flex-end;
    font-size: 13.5px;
    font-weight: 400;
    color: var(--purple);
  }
  .sign-off .field-line {
    display: inline-block;
    height: 1px;
    background: var(--rule-grey);
    margin: 0 0 3px 8px;
  }
  .staff-line { width: 197px; }
  .date-label { margin-left: 22px; }
  .date-line { width: 192px; }
</style>
</head>
<body>
  <main class="credit-note">
    <header class="brand">
      <span class="brand-square" aria-hidden="true"></span>
      <p class="brand-name">BRACKENFIELD CHEMIST</p>
    </header>
    <h1 class="title">CREDIT NOTE</h1>
    <div class="amount-rule" aria-hidden="true"></div>
    <footer class="sign-off">
      <span class="staff-label">STAFF</span>
      <span class="field-line staff-line" aria-hidden="true"></span>
      <span class="date-label">DATE</span>
      <span class="field-line date-line" aria-hidden="true"></span>
    </footer>
  </main>
</body>
</html>
```